Northway Trade Partners Needs a FRESH website

We would like a creative minded designer to take on the task to Re-design our website. Its a simple 5-7 pages. With no cart, no complex html. Just plain information about our company and products we import and export. Pictures added to the product section. Since Our logo its Blue, we would like the designer to use complementing colors in order to make the website look cleaner and modern.

Target Market(s)

The target audience will be companies looking to purchase plastic related products. Companies looking to purchase large quantities of plastic containers (Shampoo bottles, caps, sprayers, mist sprayers, cosmetic containers etc).

Industry/Entity Type

It Company

Font styles to use
Sans Serif

Requirements
Must have
• We have a section in which we would like to add pictures of some of the products we carry, therefore having an easy and clean way to navigate through the pictures will be a plus.

```html
<!DOCTYPE html>
<html lang="en">
<head>
<meta charset="utf-8">
<title>Northway Trade Partners</title>
<link rel="stylesheet" href="https://fonts.googleapis.com/css2?family=Arimo:ital,wght@0,400;0,700;1,700&family=Open+Sans:wght@400;600&display=swap">
<style>
:root{
  --dark:#232323;
  --footer:#2b2b2b;
  --blue:#0a91d8;
  --accent:#19a9e6;
  --text:#8a8a8a;
  --heading:#555;
  --rule:#d8d8d8;
  --white:#fff;
}
*{margin:0;padding:0;box-sizing:border-box}
html,body{width:1200px;height:1028px;overflow:hidden}
body{position:relative;background:var(--white);font-family:Arimo,Arial,sans-serif;color:var(--text)}
.masthead{position:absolute;left:0;top:0;width:1200px;height:318px;background:var(--dark)}
.stage-band{position:absolute;left:0;top:318px;width:1200px;height:170px;background:linear-gradient(#d6d6d6,#fff)}
.brand{position:absolute;left:254px;top:30px;display:flex;align-items:center;gap:14px}
.brand-mark{width:54px;height:54px;border-radius:50%;background:var(--white)}
.brand-name{font-family:"Open Sans",Arial,sans-serif;font-weight:600;font-size:19px;color:var(--white);line-height:1.2;width:150px}
.brand-divider{position:absolute;left:471px;top:31px;width:1px;height:54px;background:#444}
.main-nav{position:absolute;left:501px;top:52px;display:flex;gap:26px;font-size:10px}
.main-nav a{color:#e6e6e6;text-decoration:none}
.main-nav a.is-current{color:var(--accent)}
.slider-frame{position:absolute;left:254px;top:128px;width:719px;height:315px;background:#efefef;border-radius:8px 8px 30px 30px/8px 8px 14px 14px}
.slider-shadow{position:absolute;left:316px;top:445px;width:620px;height:20px;border-radius:50%;background:radial-gradient(ellipse at center,rgba(0,0,0,.15),rgba(0,0,0,0) 70%)}
.slide-visual{position:absolute;left:263px;top:138px;width:701px;height:285px;border-radius:6px;background:radial-gradient(ellipse at 25% 10%,#b9ecff 0%,#3aa9d8 22%,#136c9b 55%,#063a5a 100%)}
.slide-caption{position:absolute;left:285px;top:318px;width:337px;height:86px;background:rgba(10,20,28,.88);border:1px solid rgba(255,255,255,.08)}
.slide-caption p{position:absolute;left:22px;top:24px;font-size:14.5px;line-height:18px;color:var(--white)}
.slide-caption em{font-style:italic;font-weight:700;color:var(--accent)}
.btn-products{position:absolute;left:223px;top:29px;width:81px;height:28px;border-radius:3px;background:linear-gradient(#fff,#dcdcdc);border:1px solid #bbb;color:#1d8fd0;font-size:8.5px;font-weight:700;display:flex;align-items:center;justify-content:center}
.slider-dots{position:absolute;left:589px;top:449px;display:flex;gap:2px}
.slider-dots span{width:10px;height:10px;border-radius:50%;background:#c4c4c4}
.slider-dots span.is-active{background:var(--blue)}
.tagline{position:absolute;left:254px;top:501px;width:719px;text-align:center;font-variant:small-caps;font-size:12.5px;letter-spacing:.6px;color:#666}
.tagline-rule{position:absolute;left:254px;top:524px;width:719px;height:1px;background:var(--rule)}
.column{position:absolute;top:561px;font-size:8px;line-height:11px}
.column h2{font-size:10px;font-weight:700;color:var(--heading);letter-spacing:.4px;margin-bottom:22px}
.column p{margin-bottom:11px}
.col-about{left:254px;width:226px}
.col-mission{left:524px;width:218px}
.col-divider{position:absolute;left:503px;top:560px;width:1px;height:270px;background:#e2e2e2}
.lead{font-size:11px;color:var(--accent);margin:-8px 0 15px}
.specialty{position:absolute;left:782px;top:558px;width:191px;height:233px;background:var(--blue);color:var(--white);padding:16px 17px}
.specialty h3{font-size:9.5px;line-height:18px;font-weight:700;padding-bottom:10px;border-bottom:1px solid rgba(255,255,255,.35)}
.specialty ul{list-style:none;margin-top:13px}
.specialty li{font-size:7px;font-weight:700;height:20.2px;display:flex;align-items:center;gap:16px}
.specialty li svg{width:7px;height:8px}
.site-footer{position:absolute;left:0;top:856px;width:1200px;height:172px;background:var(--footer);text-align:center}
.footer-title{margin-top:36px;font-size:11px;font-weight:700;color:#9a9a9a}
.footer-links{margin-top:13px;font-size:8.5px;color:#8a8a8a;word-spacing:1px}
.social{display:flex;justify-content:center;gap:5px;margin-top:30px}
.social span{width:18px;height:18px;border-radius:50%;background:var(--white)}
.copyright{margin-top:22px;font-size:6.5px;color:#666}
</style>
</head>
<body>
<header class="masthead">
  <div class="brand"><span class="brand-mark"></span><span class="brand-name">Northway Trade Partners</span></div>
  <span class="brand-divider"></span>
  <nav class="main-nav">
    <a class="is-current" href="#">Home</a><a href="#">About Us</a><a href="#">Products</a><a href="#">Contact Us</a>
  </nav>
</header>
<div class="stage-band"></div>
<div class="slider-frame"></div>
<div class="slider-shadow"></div>
<div class="slide-visual" role="img" aria-label="Glowing blue world map with network lights across the continents"></div>
<div class="slide-caption">
  <p>We Think <em>Globaly</em>...<br>While Serving Your Locally..</p>
  <span class="btn-products">View Products</span>
</div>
<div class="slider-dots"><span class="is-active"></span><span></span><span></span><span></span></div>

<p class="tagline">A trustworthy company sourcing and importing your needs to your business doorsteps.</p>
<div class="tagline-rule"></div>

<section class="column col-about">
  <h2>ABOUT US</h2>
  <p>Northway Trade Partners will be your first and last stop for sourcing products from all over the world, specifically Asia and South America.<br>We have partners all around the globe that helps us make the best decision in sourcing a product from and to any market. Northway Trade Partners will always make the right choice for our clients when dealing with factories all over the world.</p>
  <p>We at Northway Trade Partners have a great relationship with our suppliers which leads us to become more efficient at sourcing products and delivering it to our clients.</p>
</section>
<span class="col-divider"></span>
<section class="column col-mission">
  <h2>OUR MISSION</h2>
  <p class="lead">You dream it and we deliver it.</p>
  <p>As easy as that sounds there are many details that goes into a importing a product to your final destination. Many clients might be faced with different issues with previous agents, logistic companies, unfaithful factories etc.</p>
  <p>That is when Northway Trade Partners steps in as being a trust-worthy company that can help you grow as a business. We will take care of all the headaches from dealing with unknown companies and make it right the first time you do business with a foreign company.</p>
</section>
<aside class="specialty">
  <h3>We at Northway Trade Partners Specialize in anything that you can think of in the plastic industry.</h3>
  <ul>
    <li><svg viewBox="0 0 7 8"><path d="M0 0L7 4L0 8L2 4Z" fill="#5fd3ff"/></svg>CAPS</li>
    <li><svg viewBox="0 0 7 8"><path d="M0 0L7 4L0 8L2 4Z" fill="#5fd3ff"/></svg>P.E.T. CONTAINERS</li>
    <li><svg viewBox="0 0 7 8"><path d="M0 0L7 4L0 8L2 4Z" fill="#5fd3ff"/></svg>P.E./P.P. CONTAINERS</li>
    <li><svg viewBox="0 0 7 8"><path d="M0 0L7 4L0 8L2 4Z" fill="#5fd3ff"/></svg>SPRAYERS</li>
    <li><svg viewBox="0 0 7 8"><path d="M0 0L7 4L0 8L2 4Z" fill="#5fd3ff"/></svg>MOLDS</li>
    <li><svg viewBox="0 0 7 8"><path d="M0 0L7 4L0 8L2 4Z" fill="#5fd3ff"/></svg>JARS</li>
  </ul>
</aside>

<footer class="site-footer">
  <p class="footer-title">NORTHWAY TRADE PARTNERS</p>
  <p class="footer-links">Product Reserch &nbsp;|&nbsp; OEM/ODM &nbsp;|&nbsp; Delivery &nbsp;|&nbsp; Freight Forwarding &nbsp;|&nbsp; Packaging &nbsp;|&nbsp; Product Design &nbsp;|&nbsp; Labeling &nbsp;|&nbsp; Custom</p>
  <div class="social"><span></span><span></span><span></span><span></span><span></span><span></span></div>
  <p class="copyright">Copyright © 2014 Northway Trade Partners LLC. &nbsp;|&nbsp; Site Map | Privacy Policy | Disclaimer</p>
</footer>
</body>
</html>
```